Harborline Crest Insurance Services

we are a high end insurance agency we specialize on Auto | Home | Business | Life looking for something professional and luxuries at the same time. if you guys need anything else please let me know.

Auto | Home | Business | Life must be under logo on the back with black background.

i want the back part to be black with our gold logo on it.

Target Market(s)

Auto | Home | Business | Life

Industry/Entity Type

Insurance Broker

Contact Information for Business Card

My logo is gold so a black in the back would be nice.

Font styles to use
Serif

Colors
000000

Requirements
Must have
• Big logo on the back with black background.

```html
<!DOCTYPE html>
<html lang="en">
<head>
<meta charset="utf-8">
<title>Harborline Crest Insurance Services — Business Cards</title>
<link rel="stylesheet" href="https://fonts.googleapis.com/css2?family=Cinzel:wght@600&family=Tinos&family=Montserrat:wght@400&display=swap">
<style>
  :root {
    --stage: #2a2a2a;
    --card: #050505;
    --gold: #e9b623;
    --gold-deep: #b8860f;
    --silver: #9a9a9a;
    --silver-light: #c4c4c4;
    --ink: #f2f2f2;
    --rule: #8a8a8a;
  }
  * { box-sizing: border-box; margin: 0; padding: 0; }
  html, body { width: 1200px; height: 852px; overflow: hidden; }
  body {
    background: var(--stage);
    position: relative;
    font-family: "Tinos", "Times New Roman", serif;
  }
  .card {
    position: absolute;
    width: 560px;
    height: 320px;
    background: var(--card);
    border-radius: 22px;
    box-shadow: 0 14px 30px rgba(0,0,0,.5);
    overflow: hidden;
  }
  .card--back { left: 60px; top: 70px; }
  .card--front { left: 580px; top: 460px; }

  /* Back: large centred brand lock-up */
  .brand-lockup {
    position: absolute;
    left: 0; right: 0; top: 26px;
    text-align: center;
  }
  .brand-mark {
    display: inline-block;
    width: 132px; height: 132px;
    border-radius: 50%;
    background: var(--gold);
    margin-bottom: 14px;
  }
  .brand-name {
    font-family: "Cinzel", "Times New Roman", serif;
    font-weight: 600;
    color: var(--gold);
    font-size: 40px;
    line-height: 1;
    letter-spacing: .5px;
    white-space: nowrap;
  }
  .brand-sub {
    font-family: "Montserrat", Arial, sans-serif;
    color: var(--silver);
    font-size: 16px;
    letter-spacing: 5px;
    margin-top: 8px;
    white-space: nowrap;
  }
  .brand-lines {
    font-family: "Montserrat", Arial, sans-serif;
    color: var(--silver);
    font-size: 13px;
    letter-spacing: 1.5px;
    margin-top: 6px;
    white-space: nowrap;
  }

  /* Front: artwork area on the right */
  .front-art {
    position: absolute;
    left: 300px; top: 0;
    width: 260px; height: 320px;
    background:
      linear-gradient(180deg, rgba(196,196,196,.55) 0%, rgba(154,154,154,.25) 30%, rgba(0,0,0,0) 42%),
      linear-gradient(160deg, rgba(0,0,0,0) 34%, var(--gold) 58%, var(--gold-deep) 80%, rgba(5,5,5,0) 100%);
  }

  /* Front: contact details */
  .front-brand {
    position: absolute;
    left: 34px; top: 40px;
  }
  .front-brand .brand-name { font-size: 27px; }
  .front-brand .brand-sub { font-size: 12px; letter-spacing: 4px; margin-top: 5px; }
  .rule {
    height: 1px;
    background: var(--rule);
    width: 280px;
  }
  .rule--top { position: absolute; left: 34px; top: 110px; }
  .person {
    position: absolute; left: 34px; top: 120px;
  }
  .person__name { color: var(--ink); font-size: 19px; }
  .person__role { color: var(--gold); font-size: 11px; margin-top: 1px; }
  .rule--mid { position: absolute; left: 34px; top: 166px; }
  .contact {
    position: absolute; left: 34px; top: 174px;
    list-style: none;
    color: var(--ink);
    font-size: 14px;
    line-height: 19px;
  }
  .contact li { display: flex; align-items: center; gap: 8px; white-space: nowrap; }
  .contact svg { width: 12px; height: 12px; fill: var(--gold); flex: none; }
  .contact .address { padding-left: 20px; }
</style>
</head>
<body>

  <section class="card card--back" aria-label="Card back">
    <div class="brand-lockup">
      <span class="brand-mark" aria-hidden="true"></span>
      <div class="brand-name">Harborline Crest</div>
      <div class="brand-sub">INSURANCE SERVICES</div>
      <div class="brand-lines">AUTO | HOME | BUSINESS | LIFE</div>
    </div>
  </section>

  <section class="card card--front" aria-label="Card front">
    <div class="front-art" role="img" aria-label="Gold and silver brand artwork area"></div>
    <div class="front-brand">
      <div class="brand-name">Harborline Crest</div>
      <div class="brand-sub">INSURANCE SERVICES</div>
    </div>
    <div class="rule rule--top"></div>
    <div class="person">
      <div class="person__name">Owen Hartley</div>
      <div class="person__role">Managing Director</div>
    </div>
    <div class="rule rule--mid"></div>
    <ul class="contact">
      <li class="address">Suite 12, 88 Marlow Lane</li>
      <li class="address">Brackenfield QLD 4021</li>
      <li>
        <svg viewBox="0 0 12 12" aria-hidden="true"><path d="M3 0h6a1 1 0 0 1 1 1v10a1 1 0 0 1-1 1H3a1 1 0 0 1-1-1V1a1 1 0 0 1 1-1zm0 2v7h6V2z"/></svg>
        0400-118-274
      </li>
      <li>
        <svg viewBox="0 0 12 12" aria-hidden="true"><path d="M2.5 0.5l2 2.5-1.2 1.3a7 7 0 0 0 4.4 4.4L9 7.5l2.5 2-1.2 2A10 10 0 0 1 .5 1.7z"/></svg>
        0700-452-913
      </li>
      <li>
        <svg viewBox="0 0 12 12" aria-hidden="true"><path d="M0 2h12v8H0zm1 1v.4l5 3.3 5-3.3V3z"/></svg>
        owen.hartley@harborcrest.com
      </li>
      <li>
        <svg viewBox="0 0 12 12" aria-hidden="true"><path d="M6 0a6 6 0 1 0 0 12A6 6 0 0 0 6 0zm-.6 1.3v2.2H3.6c.4-1.1 1-1.9 1.8-2.2zm1.2 0c.8.3 1.4 1.1 1.8 2.2H6.6zM2.4 3.5H1.8a4.8 4.8 0 0 1 1.5-1.6 6 6 0 0 0-.9 1.6zm7.2 0a6 6 0 0 0-.9-1.6 4.8 4.8 0 0 1 1.5 1.6zM1.3 4.7h1.2a9 9 0 0 0 0 2.6H1.3a4.8 4.8 0 0 1 0-2.6zm2.4 0h1.7v2.6H3.7a8 8 0 0 1 0-2.6zm2.9 0h1.7a8 8 0 0 1 0 2.6H6.6zm2.9 0h1.2a4.8 4.8 0 0 1 0 2.6H9.5a9 9 0 0 0 0-2.6zM1.8 8.5h.6a6 6 0 0 0 .9 1.6 4.8 4.8 0 0 1-1.5-1.6zm1.8 0h1.8v2.2c-.8-.3-1.4-1.1-1.8-2.2zm3 0h1.8c-.4 1.1-1 1.9-1.8 2.2zm3 0h.6a4.8 4.8 0 0 1-1.5 1.6 6 6 0 0 0 .9-1.6z"/></svg>
        harborlinecrest.com
      </li>
    </ul>
  </section>

</body>
</html>
```